The Pane Masters- we supply and install new windows for customers homes

We require a 12 page brochure (8 pages with a cover) This is to be finished 8.5 x 11 with the layout to be 17.25" x 11.25" (full bleed). These pages will be folded and saddlestitched to the finished size. We require our designer to be familiar with print layouts. I have attached a flow sheet in word that describes the content of each page. Additionally I have picture files co-ordinated to each page. Please provide a sample layout of any page for review and selection. Our colour themes as indicated in our logo are CMYK 0 80 100 0 and CMYK 65 58 58 38. We have no concept as to design but it must look professional. Upon successful selection all of the files would be made available

```html
<!DOCTYPE html>
<html lang="en">
<head>
<meta charset="utf-8">
<title>The Pane Masters – Brochure Spreads</title>
<link href="https://fonts.googleapis.com/css2?family=Raleway:wght@400;500;700&family=Roboto+Slab:wght@400;500&display=swap" rel="stylesheet">
<style>
  :root{
    --orange:#f15a22;
    --charcoal:#4b4b4b;
    --ink:#3d3d3d;
    --paper:#ffffff;
    --backdrop:#bab5b5;
    --tan-fill:#ece5dc;
    --shape-fill:#ececec;
  }
  *{margin:0;padding:0;box-sizing:border-box}
  html,body{width:1200px;height:1200px;overflow:hidden;background:var(--backdrop)}
  body{position:relative;font-family:"Raleway",sans-serif;color:var(--ink)}
  .spread{position:absolute;background:var(--paper);overflow:hidden}
  .spread--types{left:29px;top:78px;width:1134px;height:438px}
  .spread--shapes{left:33px;top:654px;width:1139px;height:440px}
  .spread-art{position:absolute;left:0;top:0}
  .abs{position:absolute}

  .types-title{position:absolute;right:25px;top:28px;font-family:"Roboto Slab",serif;font-size:18px;letter-spacing:3px;color:var(--paper);font-weight:500}
  .panel{position:absolute;width:155px;bottom:0;background:var(--charcoal)}
  .label-bar{position:absolute;width:193px;height:12px;background:var(--orange);color:var(--paper);font-size:7.8px;font-weight:500;letter-spacing:.2px;line-height:12px;padding-left:8px;text-transform:uppercase}
  .bullets{position:absolute;width:122px;list-style:none;color:var(--paper);font-size:7.6px;line-height:10px;letter-spacing:-.1px}
  .bullets li{position:relative;padding-left:8px;margin-bottom:3px}
  .bullets li::before{content:"·";position:absolute;left:0;top:0}
  .bullets strong{font-weight:700}
  .product-photo{position:absolute;background:linear-gradient(160deg,#f2f3f4,#d3d6d9);border:1px solid #cfd2d5}

  .section-title{position:absolute;top:41px;font-family:"Roboto Slab",serif;font-size:19px;letter-spacing:2.2px;color:var(--orange);font-weight:500}
  .sub-title{position:absolute;font-size:17px;line-height:20px;color:#2e2e2e;font-weight:500}
  .minor-title{position:absolute;font-size:10px;font-weight:500;color:#2e2e2e}
  .body-copy{position:absolute;font-size:8.5px;line-height:15.2px;color:var(--ink)}
  .body-copy .brand{color:var(--orange);font-weight:700}
  .divider{position:absolute;left:273px;top:74px;height:341px;border-left:1.5px dotted var(--orange)}
  .icon-label{font-family:"Raleway",sans-serif;font-size:6.6px;fill:#333;text-anchor:middle}
  .grill-art{fill:var(--tan-fill)}
  .shape-art{fill:var(--shape-fill)}
  .install-photo{position:absolute;width:156px;height:156px;border-radius:50%;border:2px solid var(--paper)}
</style>
</head>
<body>

<!-- Spread: types of windows -->
<section class="spread spread--types">
  <svg class="spread-art" width="1134" height="438" viewBox="0 0 1134 438" aria-hidden="true">
    <polygon points="0,0 1134,0 1134,68 0,36" fill="var(--charcoal)"/>
    <polygon points="0,36 1134,68 1134,74 0,42" fill="var(--orange)"/>
  </svg>
  <h1 class="types-title">TYPES OF WINDOWS</h1>

  <div class="panel" style="left:25px;top:54px"></div>
  <div class="panel" style="left:290px;top:92px"></div>
  <div class="panel" style="left:595px;top:90px"></div>
  <div class="panel" style="left:860px;top:110px"></div>

  <!-- Column 1 -->
  <div class="label-bar" style="left:45px;top:67px">Double Hung Windows</div>
  <ul class="bullets" style="left:46px;top:93px">
    <li><strong>Common style of window available.</strong></li>
    <li>Consists of two window sashes (i.e., panes of glass, one on top and one on the bottom.</li>
    <li>Top and bottom sashes are removable for easy cleaning.</li>
  </ul>
  <div class="product-photo" role="img" aria-label="Double hung window product photo" style="left:195px;top:88px;width:44px;height:80px"></div>

  <div class="label-bar" style="left:45px;top:178px">Single Hung Windows</div>
  <ul class="bullets" style="left:46px;top:204px">
    <li><strong>Common style of window available.</strong></li>
    <li>Consists of two sashes, one on top that doesn't move and the bottom one does move vertically.</li>
    <li>The advantage of the fixed window is that it limits air intrusion since there are fewer seams that need seals.</li>
  </ul>
  <div class="product-photo" role="img" aria-label="Single hung window product photo" style="left:171px;top:212px;width:80px;height:82px"></div>

  <div class="label-bar" style="left:45px;top:318px">Casement Windows</div>
  <ul class="bullets" style="left:46px;top:346px">
    <li><strong>Casement windows are hinged at the side.</strong></li>
    <li>The earliest form of movable window, with hinges or pivots at the upright side of the vertically hung sash so that it opens outward or inward like a door.</li>
  </ul>
  <div class="product-photo" role="img" aria-label="Casement window product photo" style="left:199px;top:348px;width:32px;height:68px"></div>

  <!-- Column 2 -->
  <div class="label-bar" style="left:309px;top:104px">Bay Windows</div>
  <ul class="bullets" style="left:310px;top:127px">
    <li><strong>A series of windows projecting</strong> outward from the wall.</li>
    <li>Bay windows have no more than three sides with windows.</li>
    <li>May require shingles or other roofing material (copper stand seam) on the top.</li>
  </ul>
  <div class="product-photo" role="img" aria-label="Bay window product photo" style="left:457px;top:143px;width:64px;height:68px"></div>

  <div class="label-bar" style="left:309px;top:246px">Bow Windows</div>
  <ul class="bullets" style="left:310px;top:274px">
    <li><strong>A series of windows projecting</strong> outward from the wall.</li>
    <li>Bow windows have no less than four sides with windows.</li>
    <li>May require multiple types of windows (double-hung, casement, etc).</li>
    <li>May require roofing on the top.</li>
  </ul>
  <div class="product-photo" role="img" aria-label="Bow window product photo" style="left:456px;top:302px;width:76px;height:40px"></div>

  <!-- Column 3 -->
  <div class="label-bar" style="left:613px;top:104px">Awning Windows</div>
  <ul class="bullets" style="left:614px;top:127px">
    <li><strong>Awning windows open outward from</strong> the bottom and re-hinged towards the top using a crank handle while the operating mechanism keeps the sash securely open.</li>
    <li>They provide effective ventilation without letting the elements into the home.</li>
  </ul>
  <div class="product-photo" role="img" aria-label="Awning window product photo" style="left:763px;top:138px;width:70px;height:62px"></div>

  <div class="label-bar" style="left:613px;top:246px">Slider Windows</div>
  <ul class="bullets" style="left:614px;top:274px">
    <li><strong>A horizontal sliding window where</strong> the sashes operate by sliding along a track in the window frame.</li>
    <li>Some sliders have a fixed sash and some a bypass.</li>
    <li>Note from outside which sash is operational (right or left).</li>
  </ul>
  <div class="product-photo" role="img" aria-label="Slider window product photo" style="left:763px;top:288px;width:62px;height:56px"></div>

  <!-- Column 4 -->
  <div class="label-bar" style="left:876px;top:124px">Egress Windows</div>
  <ul class="bullets" style="left:877px;top:151px">
    <li><strong>Egress windows (or doors) are required</strong> in every bedroom or in secondary suites where people sleep.</li>
    <li>Egress windows are installed to allow for an exit in case of an emergency and to provide access for a firefighter to gain entrance.</li>
  </ul>
  <div class="product-photo" role="img" aria-label="Egress window well photo" style="left:1025px;top:156px;width:74px;height:56px"></div>

  <div class="label-bar" style="left:876px;top:264px">Transom Windows</div>
  <ul class="bullets" style="left:877px;top:292px">
    <li><strong>A window that sits on top of the door</strong> or another window.</li>
    <li>Usually, are fixed glass but can also be awning or hopper style.</li>
    <li>They are usually a separate unit from the one it sits on.</li>
  </ul>
  <div class="product-photo" role="img" aria-label="Transom window product photo" style="left:1025px;top:296px;width:80px;height:56px"></div>
</section>

<!-- Spread: shapes, grills and installation -->
<section class="spread spread--shapes">
  <svg class="spread-art" width="1139" height="440" viewBox="0 0 1139 440">
    <rect x="0" y="0" width="570" height="26" fill="var(--charcoal)"/>
    <rect x="595" y="26" width="544" height="5" fill="var(--orange)"/>
    <rect x="570" y="194" width="569" height="246" fill="var(--charcoal)"/>
    <rect x="0" y="422" width="543" height="6" fill="var(--orange)"/>

    <g class="grill-art" role="img" aria-label="Illustrations of grill designs: heritage, double heritage, ladder, rectangular, diamond, circular and coordinate">
      <rect x="26" y="216" width="35" height="48"/>
      <rect x="92" y="216" width="35" height="48"/>
      <rect x="158" y="216" width="35" height="48"/>
      <rect x="223" y="216" width="35" height="48"/>
      <rect x="26" y="294" width="35" height="48"/>
      <rect x="92" y="294" width="35" height="48"/>
      <rect x="158" y="294" width="35" height="48"/>
      <rect x="223" y="294" width="35" height="48"/>
    </g>
    <text class="icon-label" x="44" y="277">Heritage</text>
    <text class="icon-label" x="110" y="274">Double</text><text class="icon-label" x="110" y="282">Heritage</text>
    <text class="icon-label" x="175" y="277">Ladder</text>
    <text class="icon-label" x="240" y="277">Rectangular</text>
    <text class="icon-label" x="44" y="355">Diamond</text>
    <text class="icon-label" x="110" y="355">Circular</text>
    <text class="icon-label" x="208" y="355">Coordinate</text>

    <g class="shape-art" role="img" aria-label="Illustrations of custom window shapes: round, half round, quarter round, extended, oval, segmental, gable, rake head, gothic, octagon, parallelogram and elliptical">
      <rect x="286" y="232" width="32" height="32"/>
      <rect x="337" y="246" width="32" height="16"/>
      <rect x="394" y="246" width="16" height="16"/>
      <rect x="434" y="232" width="16" height="30"/>
      <rect x="483" y="232" width="16" height="30"/>
      <rect x="523" y="232" width="20" height="32"/>
      <rect x="294" y="312" width="63" height="20"/>
      <rect x="378" y="302" width="63" height="30"/>
      <rect x="464" y="302" width="29" height="30"/>
      <rect x="515" y="302" width="22" height="30"/>
      <rect x="294" y="361" width="35" height="32"/>
      <rect x="353" y="361" width="32" height="32"/>
      <rect x="404" y="377" width="66" height="16"/>
      <rect x="485" y="377" width="52" height="16"/>
    </g>
    <text class="icon-label" x="302" y="279">Round</text>
    <text class="icon-label" x="353" y="279">Half Round</text>
    <text class="icon-label" x="402" y="277">Quarter</text><text class="icon-label" x="402" y="285">Round</text>
    <text class="icon-label" x="442" y="277">Extended</text><text class="icon-label" x="442" y="285">Half Round</text>
    <text class="icon-label" x="491" y="277">Extended</text><text class="icon-label" x="491" y="285">Quarter Round</text>
    <text class="icon-label" x="533" y="279">Oval</text>
    <text class="icon-label" x="326" y="348">Segmental</text>
    <text class="icon-label" x="411" y="348">Extended Segmental</text>
    <text class="icon-label" x="479" y="348">Gable</text>
    <text class="icon-label" x="527" y="348">Rake Head</text>
    <text class="icon-label" x="312" y="405">Gothic</text>
    <text class="icon-label" x="369" y="405">Octagon</text>
    <text class="icon-label" x="437" y="405">Parallelogram</text>
    <text class="icon-label" x="511" y="405">Elliptical</text>
  </svg>

  <h2 class="section-title" style="left:26px">WINDOW SHAPES AND GRILLS</h2>
  <h2 class="section-title" style="left:595px">PROFESSIONAL INSTALLATION</h2>

  <h3 class="sub-title" style="left:26px;top:74px">Simulated Divided Lites (SDL)<br>&amp; Grill Designs</h3>
  <p class="body-copy" style="left:26px;top:127px;width:236px">SDL and grill bars are often added to customize a window and match the architectural style of the home. When applied, SDL's give the traditional true divided lite appearance, while grills offer additional decor options to complement your choice of window style.</p>

  <div class="divider"></div>

  <h3 class="sub-title" style="left:286px;top:74px">Specialty Windows</h3>
  <p class="body-copy" style="left:286px;top:100px;width:264px">Whether your choice is Aluminum Clad, Wood or PVC, speciality windows offer the potential for endless design possibilities.</p>
  <h4 class="minor-title" style="left:286px;top:145px">Custom Shapes</h4>
  <p class="body-copy" style="left:286px;top:159px;width:264px">Shaped windows are custom built to suit any home and can add interesting detail. Combined with other window options such as our casement, awning, or sliding window styles, speciality windows offer a truly unique design component to any home.</p>

  <p class="body-copy" style="left:595px;top:69px;width:340px">The quality and care of professional installation make a huge difference to life of worry-free windows. When installed incorrectly, they can cause a lot of problems. Installed correctly, they are a beautiful touch offering you sunlight, a charming exterior, great insulation along with leak free and a draft free experience. Unlike other window companies, our installers completely seal the entire opening with a waterproof frame membrane <span class="brand">(SealWrap)</span> prior to installing the window. We then caulk completely around the outside and low-pressure foam insulate the inside.</p>

  <div class="abs" role="img" aria-label="Roll of waterproof butyl flashing membrane" style="left:947px;top:73px;width:166px;height:149px;border-radius:12px;background:linear-gradient(180deg,#f1efe6 0%,#f1efe6 8%,#26317f 12%,#1f2a72 88%,#eceadf 92%)"></div>

  <div class="install-photo" role="img" aria-label="Installer applying blue membrane to a window sill" style="left:597px;top:243px;background:radial-gradient(circle at 40% 60%,#4a9fe0,#2a78c4 60%,#8c7a62)"></div>
  <div class="install-photo" role="img" aria-label="Gloved hand applying foam sealant around a window frame" style="left:777px;top:243px;background:radial-gradient(circle at 55% 50%,#e2b63a,#d8d8d6 55%,#cfd0cf)"></div>
  <div class="install-photo" role="img" aria-label="Hand pressing finished siding next to an installed window" style="left:957px;top:243px;background:radial-gradient(circle at 50% 55%,#d9b8a0,#b9b9b7 50%,#8d918c)"></div>
</section>

</body>
</html>
```